WordPress Website Design Project

Technical & Functional Deliverables
WordPress CMS
Fully responsive design
Integrated WhatsApp chatbot
Custom article filtering system
SEO-friendly site structure & performance optimization
CMS user manual & training session
Updates

Need extra days to review

Industry/Entity Type

Industrial Safety and Compliance

Coding

Coded - Design and coding required

Number of Pages Required

5+ page

Font styles to use
Sans Serif

Colors
0054AA
0677BA
7BADD7
CADEEF
E8F1F8

```html
<!DOCTYPE html>
<html lang="en">
<head>
<meta charset="utf-8">
<title>Kestrane — Industrial Safety and Compliance</title>
<link href="https://fonts.googleapis.com/css2?family=Manrope:wght@400;500;600;700;800&display=swap" rel="stylesheet">
<style>
:root{
  --navy:#1b2b48;
  --navy-deep:#141f33;
  --accent:#4f87c9;
  --accent-strong:#0677BA;
  --sky:#7BADD7;
  --mist:#CADEEF;
  --ice:#E8F1F8;
  --ink:#22324d;
  --white:#ffffff;
}
*{box-sizing:border-box;margin:0;padding:0}
html,body{width:1200px;height:3940px;overflow:hidden}
body{position:relative;background:var(--white);font-family:"Manrope",Arial,sans-serif;color:var(--ink)}

/* header */
.site-header{position:absolute;left:0;top:0;width:1200px;height:107px;background:#f7f8fa;border-bottom:1px solid #e3e8ef}
.brand{position:absolute;left:138px;top:24px;display:flex;flex-direction:column}
.brand-row{display:flex;align-items:center;gap:6px}
.brand-square{width:30px;height:30px;background:var(--accent)}
.brand-name{font-weight:800;font-size:28px;letter-spacing:1px;color:var(--navy);line-height:1}
.brand-tag{font-size:9.5px;font-weight:700;color:var(--navy);text-align:center;line-height:1.2;margin-top:5px;letter-spacing:.3px}
.main-nav{position:absolute;left:398px;top:54px;display:flex;gap:27px;font-size:14px;font-weight:500;color:var(--navy)}
.main-nav .active{color:var(--accent)}
.nav-marker{position:absolute;left:410px;top:32px;width:16px;height:16px;background:var(--accent)}

/* hero */
.hero{position:absolute;left:0;top:107px;width:1200px;height:645px;overflow:hidden}
.hero-photo{position:absolute;inset:0;background:radial-gradient(ellipse at 20% 80%,#c89a4a 0%,rgba(200,154,74,0) 40%),linear-gradient(180deg,#a9b6c7 0%,#8d96a1 35%,#5d5446 70%,#2e2a26 100%)}
.hero-title{position:absolute;left:153px;top:135px;font-size:46px;font-weight:800;line-height:55px;color:var(--navy);letter-spacing:-.5px}
.hero-cta{position:absolute;left:153px;top:311px;width:168px;height:45px;background:var(--accent);color:var(--white);font-weight:700;font-size:19px;line-height:45px;padding-left:24px;clip-path:polygon(0 0,88% 0,100% 100%,0 100%)}
.hero-edge{position:absolute;left:0;top:0}

/* section heading */
.sec-head{position:absolute;left:0;width:1200px;text-align:center}
.sec-mark{display:flex;justify-content:center;align-items:center;gap:8px}
.sec-mark i{display:block;width:26px;height:2px;background:var(--sky)}
.sec-mark b{display:block;width:15px;height:15px;background:var(--accent)}
.sec-title{font-size:46px;font-weight:800;color:var(--navy);letter-spacing:-.5px;margin-top:10px;line-height:1}
.sec-title span{color:var(--accent)}

/* values */
.values-frame{position:absolute;left:150px;top:889px;width:428px;height:374px;border:2px solid var(--accent)}
.values-photo{position:absolute;left:160px;top:898px;width:426px;height:374px;background:linear-gradient(135deg,#e8ecef 0%,#9aa6b3 45%,#3b4a66 70%,#6b5a46 100%)}
.values-copy{position:absolute;left:609px;top:896px;width:455px;font-size:14.5px;line-height:19px;color:var(--navy)}
.values-copy h4{color:var(--accent);font-size:15px;font-weight:700;line-height:18px}
.values-copy p{margin-bottom:14px}
.values-copy .small{font-size:13.5px;margin-bottom:0}

/* work */
.work-band{position:absolute;left:0;top:1860px;width:1200px;height:615px;background:linear-gradient(180deg,#ffffff 0%,#eef2f6 50%,#f3f5f8 100%)}
.work-card{position:absolute;top:1456px;height:400px;overflow:hidden}
.work-card .ph{position:absolute;inset:0}
.work-card .cap{position:absolute;bottom:38px;font-size:26px;font-weight:800;line-height:30px;color:var(--white)}
.work-badge{position:absolute;left:0;bottom:0;width:160px;height:140px;background:var(--accent);border-top-right-radius:140px}
.work-title{position:absolute;left:138px;top:1872px;font-size:39px;font-weight:800;line-height:46px;color:var(--navy)}
.work-desc{position:absolute;left:138px;top:1980px;width:525px;font-size:15px;line-height:19px;color:var(--navy)}

/* clients */
.client-box{position:absolute;top:2286px;width:177px;height:86px;background:var(--white);border:1px solid var(--sky);display:flex;align-items:center;justify-content:center;gap:7px;font-weight:700;font-size:16px;color:var(--navy)}
.client-box i{display:block;width:10px;height:10px;background:var(--accent)}
.dots{position:absolute;left:566px;top:2390px;display:flex;gap:6px}
.dots i{display:block;width:12px;height:3px;background:var(--navy)}
.dots i.on{width:24px;background:var(--accent)}

/* solutions */
.sol-card{position:absolute;top:2601px;width:284px;height:374px;overflow:hidden}
.sol-card .ph{position:absolute;inset:0}
.sol-label{position:absolute;left:11px;right:11px;padding:14px 10px;text-align:center;font-size:14.5px;font-weight:800;line-height:19px;color:var(--white);background:var(--navy)}
.sol-label.blue{background:var(--accent)}

/* people */
.person{position:absolute;top:3163px;width:284px}
.person .ph{height:377px}
.person h5{font-size:21px;font-weight:800;color:var(--navy);margin-top:30px;line-height:24px}
.person p{font-size:14px;color:var(--navy);margin-top:4px}
.plus{position:absolute;right:0;top:0;width:46px;height:46px;background:var(--white);color:var(--accent);font-size:28px;line-height:44px;text-align:center;font-weight:400}

/* footer */
.site-footer{position:absolute;left:0;top:3662px;width:1200px;height:278px;background:linear-gradient(180deg,#1a222e 0%,#10161f 100%);color:var(--white)}
.foot-about{position:absolute;left:138px;top:60px;width:290px;font-size:14.5px;line-height:24px}
.foot-col{position:absolute;font-size:13.5px;line-height:24px}
.foot-brand{position:absolute;left:878px;top:44px;display:flex;flex-direction:column;align-items:center}
.foot-brand .brand-name{color:var(--white);font-size:32px}
.foot-brand .brand-square{background:var(--white);width:34px;height:34px}
.foot-brand .brand-tag{color:var(--white);font-size:11px}
.social-dot{position:absolute;left:1032px;top:167px;width:32px;height:32px;border-radius:50%;background:var(--accent)}
.foot-legal{position:absolute;left:138px;top:232px;font-size:13.5px}
.foot-copy{position:absolute;left:880px;top:232px;font-size:13.5px}
</style>
</head>
<body>

<header class="site-header">
  <div class="brand">
    <div class="brand-row"><span class="brand-square"></span><span class="brand-name">KESTRANE</span></div>
    <div class="brand-tag">YOUR PARTNER IN INDUSTRIAL<br>SAFETY AND COMPLIANCE</div>
  </div>
  <span class="nav-marker"></span>
  <nav class="main-nav">
    <span class="active">Home</span><span>About Us</span><span>Solutions</span><span>Articles</span><span>Our Work</span><span>White Papers</span><span>News</span><span>Contact Us</span>
  </nav>
</header>

<section class="hero">
  <div class="hero-photo" role="img" aria-label="Photo of a safety engineer in a hard hat holding a tablet at an industrial plant at dusk"></div>
  <h1 class="hero-title">YOUR PARTNER IN<br>INDUSTRIAL SAFETY &amp;<br>COMPLIANCE</h1>
  <div class="hero-cta">Contact Us</div>
  <svg class="hero-edge" width="1200" height="645" viewBox="0 0 1200 645">
    <path d="M585 520 v36 l-12 -10 M585 556 l12 -10" stroke="#ffffff" stroke-width="1.5" fill="none"/>
    <polygon points="0,645 550,591 1200,645" fill="#ffffff"/>
    <polygon points="600,588 1200,535 1200,630" fill="#4f87c9"/>
    <polygon points="600,588 1200,630 1200,645 600,592" fill="#1b2b48"/>
  </svg>
</section>

<div class="sec-head" style="top:755px">
  <div class="sec-mark"><i></i><b></b><i></i></div>
  <h2 class="sec-title"><span>OUR</span> VALUES</h2>
</div>

<div class="values-frame"></div>
<div class="values-photo" role="img" aria-label="Photo of a worker in a yellow hard hat inspecting pipework with a clipboard"></div>
<div class="values-copy">
  <h4>WE ARE KESTRANE</h4>
  <p>Your Partner in Industrial Safety and Compliance</p>
  <h4>MISSION STATEMENT AND CORE VALUES</h4>
  <p style="margin-top:10px">To provide expert guidance and practical solutions in industrial safety and compliance, delivering clarity, reliability, and peace of mind to every partner we serve.</p>
  <p>We achieve this mission by staying true to our foundational values:</p>
  <p class="small">Assurance: Providing confidence through technically robust solutions.<br>Reliability: Ensuring consistent performance in demanding situations.<br>Commitment: Fulfilling promises and exceeding expectations.<br>Honor: Upholding the highest ethical standards.<br>Expertise: Leveraging deep industry knowledge to solve complex challenges.<br>Responsibility: Taking full accountability from concept through completion.</p>
</div>

<div class="sec-head" style="top:1348px">
  <div class="sec-mark"><i></i><b></b><i></i></div>
  <h2 class="sec-title"><span>OUR</span> WORK</h2>
</div>

<div class="work-band" role="img" aria-label="Faint backdrop of a refinery skyline with a worker silhouette"></div>

<div class="work-card" style="left:0;width:116px">
  <div class="ph" role="img" aria-label="Photo of engineers at a plant" style="background:linear-gradient(160deg,#8a6a40,#3d3126)"></div>
  <div class="cap" style="right:16px;width:400px;text-align:right">TRANSITIONING TO<br>FLUORINE-FREE<br>FOAM.</div>
</div>
<div class="work-card" style="left:138px;width:541px">
  <div class="ph" role="img" aria-label="Photo of two engineers inspecting gauges on plant pipework" style="background:linear-gradient(135deg,#c27a2a 0%,#5d6b78 45%,#1f3a4d 100%)"></div>
  <div class="work-badge">
    <svg width="160" height="140" viewBox="0 0 160 140">
      <path d="M42 92 a28 28 0 0 1 56 0 z" fill="none" stroke="#fff" stroke-width="4"/>
      <path d="M34 92 h72 v8 h-72 z" fill="none" stroke="#fff" stroke-width="4"/>
      <path d="M70 64 v-8" stroke="#fff" stroke-width="4"/>
      <path d="M50 104 a22 22 0 0 0 40 0" fill="none" stroke="#fff" stroke-width="4"/>
    </svg>
  </div>
</div>
<div class="work-card" style="left:700px;width:286px">
  <div class="ph" role="img" aria-label="Photo of two engineers walking through a factory hall" style="background:linear-gradient(180deg,#3a3f48 0%,#23272e 60%,#4a3a22 100%)"></div>
  <div class="cap" style="left:22px">RISK<br>MANAGEMENT &amp;<br>COMPLIANCE</div>
</div>
<div class="work-card" style="left:1002px;width:198px">
  <div class="ph" role="img" aria-label="Photo of a worker in a yellow hard hat and high-visibility vest" style="background:linear-gradient(160deg,#b9c3cc 0%,#c7b03a 55%,#6a7a4a 100%)"></div>
  <div class="cap" style="left:30px;width:400px">TECHNICAL<br>SUPPORT &amp; SITE<br>SERVICES</div>
</div>

<h3 class="work-title">ENGINEERING &amp; DESIGN<br>SERVICES</h3>
<p class="work-desc">Lorem ipsum dolor sit amet, consectetur adipiscing elit, sed do eiusmod tempor incididunt ut labore et dolore magna aliqua. Quis ipsum suspendisse ultrices gravida. Risus commodo viverra maecenas accumsan lacus vel facilisis.</p>

<div class="sec-head" style="top:2170px">
  <div class="sec-mark"><i></i><b></b><i></i></div>
  <h2 class="sec-title"><span>OUR</span> CLIENTS</h2>
</div>

<div class="client-box" style="left:138px"><i></i>NORVIK</div>
<div class="client-box" style="left:324px">Halden Studio</div>
<div class="client-box" style="left:511px;font-size:20px">K+L</div>
<div class="client-box" style="left:697px">Corra</div>
<div class="client-box" style="left:884px">Mervo</div>
<div class="dots"><i class="on"></i><i></i><i></i></div>

<div class="sec-head" style="top:2485px">
  <div class="sec-mark"><i></i><b></b><i></i></div>
  <h2 class="sec-title"><span>OUR</span> SOLUTIONS</h2>
</div>

<div class="sol-card" style="left:0">
  <div class="ph" role="img" aria-label="Photo of an engineer in a hard hat overlooking a lit refinery" style="background:linear-gradient(160deg,#c8742c 0%,#6b5a52 45%,#2c4a6e 100%)"></div>
  <div class="sol-label" style="bottom:20px">ENGINEERING &amp; DESIGN</div>
</div>
<div class="sol-card" style="left:306px">
  <div class="ph" role="img" aria-label="Blue-tinted photo of two engineers reviewing a tablet on site" style="background:linear-gradient(180deg,#8ea6c6 0%,#5d7599 60%,#3f5478 100%)"></div>
  <div class="sol-label blue" style="top:11px">TECHNICAL SUPPORT &amp;<br>SITE SERVICES</div>
</div>
<div class="sol-card" style="left:612px">
  <div class="ph" role="img" aria-label="Photo of engineers pointing at a control panel" style="background:linear-gradient(140deg,#c48a3a 0%,#7a8a5a 35%,#2f6a9a 70%,#1c3a5e 100%)"></div>
  <div class="sol-label" style="bottom:14px">RISK MANAGEMENT &amp;<br>COMPLIANCE SERVICES</div>
</div>
<div class="sol-card" style="left:916px">
  <div class="ph" role="img" aria-label="Photo of two workers in orange vests reviewing a tablet at a plant" style="background:linear-gradient(160deg,#8ea3ba 0%,#5c6c80 45%,#c2672c 75%,#40495a 100%)"></div>
  <div class="sol-label" style="top:11px">TRANSITIONING TO<br>FLUORINE-FREE FOAM</div>
</div>

<div class="sec-head" style="top:3040px">
  <div class="sec-mark"><i></i><b></b><i></i></div>
  <h2 class="sec-title"><span>OUR</span> PEOPLE</h2>
</div>

<div class="person" style="left:0">
  <div class="ph" role="img" aria-label="Portrait of Daniel Reyes" style="background:linear-gradient(180deg,#eef0f2 0%,#d8dde2 60%,#8fb8d8 100%)"></div>
  <h5 style="padding-left:31px">DANIEL REYES</h5><p style="padding-left:31px">Project Engineer</p>
</div>
<div class="person" style="left:306px">
  <div class="ph" role="img" aria-label="Portrait of Tom Ellery" style="background:linear-gradient(180deg,#8a8f96 0%,#6e747c 60%,#4c6a7c 100%)"></div>
  <span class="plus">+</span>
  <h5 style="padding-left:22px">TOM ELLERY</h5><p style="padding-left:22px">Structural Engineer</p>
</div>
<div class="person" style="left:612px">
  <div class="ph" role="img" aria-label="Portrait of Mara" style="background:linear-gradient(180deg,#9a958e 0%,#b8b2aa 60%,#e4e2df 100%)"></div>
  <h5 style="padding-left:29px">MARA</h5><p style="padding-left:29px">Mechanical Engineer</p>
</div>
<div class="person" style="left:916px">
  <div class="ph" role="img" aria-label="Portrait of Helena" style="background:linear-gradient(180deg,#7fc060 0%,#6aa652 55%,#2f5a3e 100%)"></div>
  <h5 style="padding-left:30px">HELENA</h5><p style="padding-left:30px">Project Manager</p>
</div>

<footer class="site-footer">
  <p class="foot-about">We are Kestrane. Your Partner in Industrial Safety and Compliance Lorem ipsum dolor sit amet, consectetur adipiscing elit, sed do eiusmod tempor incididunt ut labore et dolore magna aliqua.</p>
  <div class="foot-col" style="left:530px;top:66px">Home<br>About Us<br>Solutions<br>Articles</div>
  <div class="foot-col" style="left:691px;top:60px">Our Work<br>White Papers<br>News<br>Contact Us</div>
  <div class="foot-brand">
    <div class="brand-row"><span class="brand-square"></span><span class="brand-name">KESTRANE</span></div>
    <div class="brand-tag">YOUR PARTNER IN INDUSTRIAL<br>SAFETY AND COMPLIANCE</div>
  </div>
  <span class="social-dot" role="img" aria-label="Professional network profile"></span>
  <div class="foot-legal">Legal &nbsp;| &nbsp;Cookies &nbsp;| &nbsp;Privacy</div>
  <div class="foot-copy">© 2025 | www.kestrane-safety.com</div>
</footer>

</body>
</html>
```